BrightLoop (1 page) homepage re-design

Our homepage needs a face-lift! We need our homepage on our website re-designed with a fresh and current look and feel. We have all the details, colour codes and a rough wireframe ready, but need a talented designer to put some personality into our ideas.

What we do: BrightLoop is a digital marketing agency with offices in Australia (Sydney) and South Africa (Cape Town). We specialise in SEO, PPC (otherwise known as Zentro PayLine or SEM), content marketing and Zentro Tallyboard. We use these tools to help our clients realise their business dreams.

VISUAL

Style / theme of the design:
Clean, simplistic, fun, flow.

Websites we draw inspiration from:
This is the theme we want to use to build the website
http://demo.vormalayouts.example/vl/?theme=Pebbled
Inspiration:
https://www.ondrapromo.example/
https://www.nelvagrowth.example.au/
https://quimbel.example.au/
https://torvin.layout-works.example/forum/

What we like about the site:
Clean, simple design, good use of white space. The subtle changing background colours, strong contrast with text. Not too busy or distracting.

What we don’t want: Too many different colours.

Target Market(s)

Our target audience: Marketing Managers of small to medium size businesses in Australia.

Industry/Entity Type

Marketing

Number of Pages Required

1 page

Font styles to use
Sans Serif

Requirements
Must have
• Elements to be added on homepage in order and as seen in attachments:
• - Section 1: Video with team as image and a play button add the heading: We help smart marketing managers achieve their KPIs [line break] and reduce their digital marketing overwhelm.
• - Section 2: Solutions section with the 6 solutions displayed in a row.
• - Section 3: Register Free Webinar with video
• - Section 4: Please add 3 case studies (as seen in attached docs there is only 1 but please add 3 below each other)
• - Section 5: Clients. Please add all client logo’s (black and white)
• - Section 6: Our Blog (as seen attached)
• - Section 7: Conferences Attended (please add the title and a paragraph of lorem Ipsom below) and then please add all conference logo’s attached below.
• - Section 8: In The Media (please add all logo’s titled media) white background
• - Section 9: Footer (dark grey footer) add our Zentro honoured affiliate logo here please
• - Section10: Footer - include:
• - Social logos (WorkMesh, Blipster, Pallwall, ReelDrop, Zentro Hub)
• - Navigation
• - Contact details (name, address, phone number, email)
• Colour codes:
• We want to use light greys, white and charcoal grey for the backgrounds with a pop of our green colour to bring out our branding and all CTA’s to be orange, colour codes below:
• Light grey: #F2F2F2
• Charcoal grey: #161616
• Green: #428E29
• CTA’s: #de7532
• PLEASE NOTE: Please see attached pdf titled: homepagecopybrief.pdf for all the titles and statistics that need to go on the homepage
Should not have
• Too much colour, icons should not be different colours

```html
<!DOCTYPE html>
<html lang="en">
<head>
<meta charset="utf-8">
<title>BrightLoop — Digital Marketing</title>
<link rel="stylesheet" href="https://fonts.googleapis.com/css2?family=Lato:wght@300;400;700&display=swap">
<style>
  :root {
    --brand-green: #428E29;
    --hero-green-dark: #4bb877;
    --hero-green-mid: #58c98a;
    --hero-green-light: #6cf3ad;
    --hero-teal: #3fbf9a;
    --cta-orange: #de7532;
    --white: #ffffff;
    --light-grey: #F2F2F2;
    --charcoal: #161616;
    --photo-grey: #6b6a6d;
  }
  * { box-sizing: border-box; margin: 0; padding: 0; }
  html, body { width: 1125px; height: 1200px; overflow: hidden; background: var(--white); }
  body { font-family: 'Lato', sans-serif; position: relative; }

  .site-header {
    position: absolute; top: 0; left: 0; width: 1125px; height: 66px;
    background: var(--white); z-index: 3;
  }
  .brand-name {
    position: absolute; left: 100px; top: 20px;
    font-size: 23px; font-weight: 700; color: var(--brand-green); letter-spacing: -0.5px;
  }
  .header-address {
    position: absolute; left: 707px; top: 29px;
    font-size: 11px; color: var(--brand-green); letter-spacing: -0.2px;
  }
  .header-phone {
    position: absolute; left: 898px; top: 24px;
    font-size: 19px; font-weight: 700; color: var(--brand-green); letter-spacing: -0.4px;
  }
  .menu-toggle { position: absolute; left: 1046px; top: 28px; width: 28px; text-align: center; }
  .menu-toggle span { display: block; height: 1.5px; background: var(--brand-green); margin-bottom: 4px; }
  .menu-toggle small { display: block; font-size: 8px; color: var(--brand-green); margin-top: -1px; }

  .hero { position: absolute; top: 66px; left: 0; width: 1125px; height: 600px; }
  .hero-backdrop { position: absolute; inset: 0; }
  .hero-title {
    position: absolute; top: 111px; width: 1125px; text-align: center;
    color: var(--white); font-size: 34px; font-weight: 700; letter-spacing: -1.3px;
  }
  .hero-subtitle {
    position: absolute; top: 155px; width: 1125px; text-align: center;
    color: var(--white); font-size: 29px; font-weight: 300; letter-spacing: -0.6px;
  }
  .team-video {
    position: absolute; left: 344px; top: 217px; width: 465px; height: 262px;
    background: linear-gradient(180deg, #5a595c 0%, #6f6c72 45%, #4a4350 100%);
  }
  .play-button {
    position: absolute; left: 209px; top: 104px; width: 54px; height: 54px;
    border-radius: 50%; background: rgba(255,255,255,0.35); border: 1.5px solid rgba(255,255,255,0.8);
  }
  .play-button::after {
    content: ""; position: absolute; left: 21px; top: 15px;
    border-left: 18px solid var(--white); border-top: 12px solid transparent; border-bottom: 12px solid transparent;
  }

  .solutions { position: absolute; top: 670px; left: 0; width: 1125px; }
  .section-title {
    text-align: center; color: var(--brand-green); font-size: 24px; font-weight: 400; letter-spacing: -0.6px;
  }
  .section-intro {
    position: absolute; left: 205px; top: 50px; width: 800px;
    color: var(--brand-green); font-size: 23.5px; font-weight: 300; line-height: 28.5px; letter-spacing: -0.2px;
  }
  .solution-card {
    position: absolute; width: 137px; height: 119px; background: var(--white);
    box-shadow: 0 1px 4px rgba(0,0,0,0.12); text-align: center; padding-top: 22px;
  }
  .solution-card svg { display: block; margin: 0 auto 6px; width: 24px; height: 24px; }
  .solution-name { font-size: 12.5px; color: var(--brand-green); line-height: 14px; }
  .solution-note { font-size: 10.5px; color: #5fae45; line-height: 14px; margin-top: 3px; }
</style>
</head>
<body>

<header class="site-header">
  <div class="brand-name">BrightLoop</div>
  <div class="header-address">24-26 Harbourline St, The Quay, Sydney</div>
  <div class="header-phone">1300 555 018</div>
  <div class="menu-toggle"><span></span><span></span><small>MENU</small></div>
</header>

<section class="hero">
  <svg class="hero-backdrop" width="1125" height="600" viewBox="0 0 1125 600">
    <defs>
      <linearGradient id="heroFill" x1="0" y1="0" x2="1" y2="1">
        <stop offset="0" stop-color="#4ab374"/>
        <stop offset="0.55" stop-color="#58c98a"/>
        <stop offset="1" stop-color="#6cf7b0"/>
      </linearGradient>
    </defs>
    <polygon points="0,0 1125,0 1125,356 0,594" fill="url(#heroFill)"/>
    <polygon points="188,0 563,0 563,88 188,107" fill="var(--hero-teal)" opacity="0.7"/>
    <polygon points="563,0 700,0 563,28" fill="#7dd9a3" opacity="0.8"/>
    <polygon points="940,95 1125,55 1125,206 940,246" fill="#44d3b0" opacity="0.7"/>
    <polygon points="0,446 375,376 375,515 0,594" fill="#5ccc8e" opacity="0.6"/>
  </svg>
  <h1 class="hero-title">We help smart marketing managers achieve their KPIs</h1>
  <p class="hero-subtitle">and reduce their digital marketing overwhelm.</p>
  <div class="team-video" role="img" aria-label="Team photo of the BrightLoop staff standing together, used as the video cover">
    <div class="play-button"></div>
  </div>
</section>

<section class="solutions">
  <h2 class="section-title">SOLUTIONS</h2>
  <p class="section-intro">Lorem ipsum dolor sit amet, consectetur adipisicing elit, sed do eiusmod tempor incididunt ut labore et dolore magna aliqua. Ut enim ad minim veniam, quis nostrud ullamco laboris nisi ut aliquip ex ea commodo&nbsp; consequat.</p>

  <div class="solution-card" style="left:223px; top:206px;">
    <svg viewBox="0 0 24 24" fill="var(--cta-orange)"><rect x="4" y="13" width="4" height="9"/><rect x="10" y="10" width="4" height="12"/><rect x="16" y="6" width="4" height="16"/><circle cx="6" cy="9" r="1.6"/><circle cx="12" cy="6" r="1.6"/><circle cx="18" cy="2.5" r="1.6"/></svg>
    <div class="solution-name">Grow RTevenue</div>
    <div class="solution-note">And improve you<br>bottom line</div>
  </div>
  <div class="solution-card" style="left:498px; top:206px;">
    <svg viewBox="0 0 24 24" fill="none" stroke="var(--cta-orange)" stroke-width="1.8"><circle cx="8" cy="2.5" r="1.2" fill="var(--cta-orange)"/><circle cx="12" cy="2" r="1.2" fill="var(--cta-orange)"/><circle cx="16" cy="2.5" r="1.2" fill="var(--cta-orange)"/><path d="M3 6h18l-7 8v3h-4v-3z" fill="var(--cta-orange)"/><circle cx="12" cy="20" r="3"/></svg>
    <div class="solution-name">Convert Leads</div>
    <div class="solution-note">Increase convertion<br>the trusted way</div>
  </div>
  <div class="solution-card" style="left:773px; top:206px; padding-top:20px;">
    <svg viewBox="0 0 24 24" fill="var(--cta-orange)" stroke="var(--cta-orange)" stroke-width="1.4"><path d="M3 9h4l8-5v16l-8-5H3z"/><path d="M18 8l4-3M18 12h4M18 16l4 3" fill="none"/></svg>
    <div class="solution-name">Increase Brand<br>Awareness</div>
    <div class="solution-note">Get to the right audience</div>
  </div>

  <div class="solution-card" style="left:223px; top:379px;">
    <svg viewBox="0 0 24 24" fill="none" stroke="var(--cta-orange)" stroke-width="1.3"><circle cx="8" cy="13" r="7"/><path d="M8 6v7h7"/><path d="M10 3h5v5h-5z"/><path d="M16 8h7M16 12h7M16 16h6M16 20h4"/></svg>
    <div class="solution-name">Data and KPIs</div>
    <div class="solution-note">And improve you<br>bottom line</div>
  </div>
  <div class="solution-card" style="left:498px; top:379px;">
    <svg viewBox="0 0 24 24" fill="none" stroke="var(--cta-orange)" stroke-width="1.5"><ellipse cx="9" cy="9" rx="8" ry="6"/><path d="M5 14l-2 4 5-3"/><ellipse cx="16" cy="14" rx="7" ry="5"/><circle cx="6" cy="9" r="0.8" fill="var(--cta-orange)"/><circle cx="9" cy="9" r="0.8" fill="var(--cta-orange)"/><circle cx="12" cy="9" r="0.8" fill="var(--cta-orange)"/></svg>
    <div class="solution-name">Increase Engagements</div>
    <div class="solution-note">Improved Interaction<br>with your content</div>
  </div>
  <div class="solution-card" style="left:773px; top:379px; padding-top:20px;">
    <svg viewBox="0 0 24 24" fill="none" stroke="var(--cta-orange)" stroke-width="1.3"><rect x="2" y="6" width="16" height="16"/><rect x="6" y="2" width="8" height="5"/><rect x="18" y="4" width="4" height="18"/><path d="M4 10h12M4 14h12M4 18h12M8 10v10M12 10v10"/></svg>
    <div class="solution-name">Marketing Strategy/<br>Budget</div>
    <div class="solution-note">Get to the right audience</div>
  </div>
</section>

</body>
</html>
```